Brochure design for HVAC Company

A classic tri-fold brochure design for an air conditioning, refrigeration, and heating company. Would like the designs to be simple (uncluttered), professional, and pull in the logo colors. Attached is the logo and a business card designs. The company name is Bluestem Valley Air Conditioning, Refrigeration, and Heating.

Target Market(s)

Businesses normally food establishments for refrigeration and ice machines. Looking to sell them on maintenance plan: Gold, Silver, and Bronze. The material should help them to understand the services offered: Maintenance, Servicing and Troubleshooting, and Installations of ice machines, commercial refrigeration, and walk-in freezers and air conditioning (duct, ductless, and rooftop)

Industry/Entity Type

Hvac

Font styles to use
Sans Serif

Requirements
Must have
• Include standard information, such as company name, at least two types of contact information (phone, email and post office address), a logo and tagline. It should also include a headline on the front and two or three brief items outlining benefits your organization can provide.
• Tagline is approximately 14 words and 66 characters.
• Looking to inform customers of services offered: maintenance three plans gold, silver, and bronze, servicing and troubleshooting, and installation.
• Products Serviced, maintained, and installed: Commercial refrigeration, Ice Machines, Air Conditioning (both duct, ductless, and rooftop), walk in freezers.
• Call to action is $100 off on signed maintenance contract. $50 off on first service call.
• Use lorem ipsum text to complement the details of the above information. I will add it later before printing.
• Use logo color scheme and any other colors that complement it.
• Would like this to be a word template.
Nice to have
• Can you make this a Microsoft Word template? Sketch is good, or adobe cs4 format.
Should not have
• Photos should NOT be focused on the homeowner. Should BE focused on the commercial side of the business. Photos can be from any of these product areas: commercial refrigeration, ice machine, walk in freezer boxes, and light roof top ac and heating units.

```html
<!DOCTYPE html>
<html lang="en">
<head>
<meta charset="utf-8">
<title>Bluestem Valley – Tri-fold Brochure</title>
<link rel="stylesheet" href="https://fonts.googleapis.com/css2?family=Open+Sans:wght@400;600;700&family=Oswald:wght@500&family=Montserrat:wght@700;800&display=swap">
<style>
:root{
  --blue:#2a54b0;
  --blue-dark:#1b3a8c;
  --navy:#16306f;
  --orange:#f26a1b;
  --grey-bg:#d8d9db;
  --panel-white:#ffffff;
  --ink:#2b3550;
  --gold:#d9a12e;
  --silver:#b9bdc3;
  --bronze:#c9843f;
  --table-bg:#ececec;
  --line:#cfcfcf;
}
*{box-sizing:border-box;margin:0;padding:0}
html,body{width:879px;height:1200px;overflow:hidden;background:var(--grey-bg)}
body{font-family:"Open Sans",Arial,sans-serif;color:var(--ink)}
.stage{position:absolute;left:0;top:0;width:1085px;height:1481px;transform:scale(0.8101);transform-origin:0 0}
.spread{position:absolute;width:800px;height:620px;background:var(--panel-white);box-shadow:0 14px 14px -8px rgba(0,0,0,.35);overflow:hidden}
.spread--outside{left:149px;top:83px}
.spread--inside{left:149px;top:768px;width:801px}
.abs{position:absolute}
.photo{position:absolute}
.blue-panel{position:absolute;top:0;background:linear-gradient(180deg,#2f5cc0 0%,var(--blue) 55%,var(--blue-dark) 100%);color:#fff}

/* wordmark */
.brand{position:absolute;text-align:center;color:#fff}
.brand__row{display:flex;align-items:center;justify-content:center;gap:8px;white-space:nowrap}
.brand__dot{width:30px;height:30px;border-radius:50%;border:3px solid #fff;flex:none}
.brand__name{font-family:"Montserrat",Arial,sans-serif;font-weight:800;font-size:24px;line-height:1;letter-spacing:-.5px}
.brand__tag{font-family:"Montserrat",Arial,sans-serif;font-weight:700;font-size:7.2px;letter-spacing:.7px;margin-top:9px;white-space:nowrap}

.headline{font-weight:600;font-size:18px;text-align:center;line-height:25px;color:#fff}
.body-copy{font-size:10px;line-height:13px}

/* services list */
.services-tab{position:absolute;left:0;top:307px;width:155px;height:31px;background:var(--orange);border-radius:0 16px 16px 0;color:#fff;font-weight:600;font-size:19px;padding:3px 0 0 15px}
.svc{position:absolute;left:15px;font-size:11px;color:var(--ink);display:flex;gap:9px;align-items:flex-start;line-height:14px}
.svc__icon{width:18px;height:15px;flex:none;border-radius:3px;background:var(--blue)}
.svc__icon--round{border-radius:50%}
.svc-rule{position:absolute;left:15px;top:457px;width:220px;height:1px;background:var(--line)}

/* coupons */
.coupon{position:absolute;left:273px;width:235px;height:54px;background:#fff;border-radius:4px;box-shadow:0 2px 3px rgba(0,0,0,.25);display:flex;align-items:center;padding-left:10px;gap:9px}
.coupon__amount{font-family:"Oswald",Arial,sans-serif;font-weight:500;font-size:30px;color:var(--orange);letter-spacing:-.5px;white-space:nowrap}
.coupon__note{font-family:"Oswald",Arial,sans-serif;font-weight:500;font-size:11px;color:var(--orange);line-height:13px;white-space:nowrap}

/* right outside panel */
.feature{position:absolute;text-align:center;width:70px}
.feature__disc{width:58px;height:58px;margin:0 auto;border-radius:50%;background:radial-gradient(circle at 40% 35%,#3b6fd6,var(--navy));border:3px solid #fff;box-shadow:0 1px 3px rgba(0,0,0,.3)}
.feature__label{font-size:7.3px;font-weight:700;color:var(--ink);margin-top:9px;letter-spacing:-.2px;white-space:nowrap}
.market{position:absolute;left:524px;width:276px;text-align:center;font-size:17px;font-weight:600;color:var(--ink);top:535px}
.availability{position:absolute;left:524px;width:276px;text-align:center;font-size:10px;color:#444;top:564px}

/* footer */
.footer{position:absolute;left:0;bottom:0;width:100%;height:33px}
.footer__text{position:absolute;top:9px;color:#fff;font-weight:700;font-size:11px;white-space:nowrap}
.footer__phone{display:flex;align-items:center;gap:9px;font-size:13px;top:8px}
.footer__web{font-size:12px;top:8px}

/* inside left */
.inside-copy{position:absolute;left:19px;top:198px;width:231px}
.inside-copy .body-copy{text-align:justify;margin-bottom:13px}
.install-title{font-weight:700;font-size:11.5px;margin:8px 0 9px}
.install-list{list-style:none;font-size:10px;line-height:17px;margin-bottom:20px}
.install-list li{display:flex;align-items:center;gap:6px;white-space:nowrap}
.install-list li::before{content:"";width:9px;height:9px;border-radius:50%;background:var(--orange);flex:none}

/* pricing */
.plans{position:absolute;left:277px;top:298px;width:506px;height:276px;display:flex;gap:2px;background:#dcdcdc}
.plan{flex:1;background:var(--table-bg);position:relative;text-align:center}
.plan__head{height:54px;color:#fff;font-weight:700;font-size:16px;padding-top:5px;line-height:20px}
.plan--gold .plan__head{background:var(--gold)}
.plan--silver .plan__head{background:var(--silver)}
.plan--bronze .plan__head{background:var(--bronze)}
.plan__price{width:46px;height:46px;border-radius:50%;background:var(--blue);border:3px solid #fff;box-shadow:0 1px 3px rgba(0,0,0,.35);color:#fff;font-family:"Oswald",Arial,sans-serif;font-weight:500;font-size:15px;line-height:40px;margin:-26px auto 0;position:relative}
.plan__rows{list-style:none;margin:8px 8px 0}
.plan__rows li{font-size:7.6px;font-weight:600;color:#333;height:19.5px;line-height:19px;border-bottom:1px solid var(--line);white-space:nowrap}
.plan__rows li.gap{margin-top:3px}
</style>
</head>
<body>
<div class="stage">

  <!-- ============ OUTSIDE SPREAD ============ -->
  <section class="spread spread--outside" aria-label="Brochure outside">

    <div class="photo" role="img" aria-label="Photo of a stainless steel commercial kitchen" style="left:0;top:0;width:261px;height:295px;background:linear-gradient(160deg,#e9ecef 0%,#c3c8cd 50%,#9aa1a8 100%)"></div>
    <svg class="abs" style="left:0;top:0" width="261" height="110" viewBox="0 0 261 110">
      <path d="M0 0H261V35C170 30 70 45 0 95Z" fill="var(--blue)"/>
      <path d="M0 80C70 45 160 38 261 42V50C165 47 75 55 0 95Z" fill="var(--orange)"/>
    </svg>

    <div class="services-tab">SERVICES</div>
    <div class="svc" style="top:361px"><span class="svc__icon svc__icon--round"></span>MAINTENANCE</div>
    <div class="svc" style="top:385px"><span class="svc__icon svc__icon--round"></span>SERVICING</div>
    <div class="svc" style="top:409px"><span class="svc__icon"></span>TROUBLESHOOTING</div>
    <div class="svc" style="top:433px"><span class="svc__icon svc__icon--round"></span>INSTALLATIONS</div>
    <div class="svc-rule"></div>
    <div class="svc" style="top:465px"><span class="svc__icon"></span>ICE MACHINES</div>
    <div class="svc" style="top:489px"><span class="svc__icon"></span>COMMERCIAL REFRIGERATION</div>
    <div class="svc" style="top:513px"><span class="svc__icon"></span>WALK-IN FREEZERS</div>
    <div class="svc" style="top:537px"><span class="svc__icon"></span><span>AIR CONDITIONING<br>(DUCT, DUCTLESS, AND ROOFTOP)</span></div>

    <div class="blue-panel" style="left:261px;width:263px;height:587px">
      <svg class="abs" style="left:56px;top:25px" width="150" height="140" viewBox="0 0 150 140" role="img" aria-label="Photo of a technician repairing a refrigeration unit, framed in a gear shape">
        <circle cx="75" cy="70" r="66" fill="#fff"/>
        <circle cx="75" cy="70" r="58" fill="#5d6670"/>
      </svg>
      <div class="brand" style="left:0;top:205px;width:263px">
        <div class="brand__row"><span class="brand__dot"></span><span class="brand__name">Bluestem Valley</span></div>
        <div class="brand__tag">AIR CONDITIONING · REFRIGERATION · HEATING</div>
      </div>
      <div class="headline abs" style="left:0;top:288px;width:263px">EMERGENCY SERVICE<br>WHEN YOU NEED IT</div>
      <p class="body-copy abs" style="left:16px;top:348px;width:235px">Bluestem Valley is family owned and operated and provides a full range of HVAC installation, maintenance, repairs and services to residential and commercial customers.</p>
      <p class="abs" style="left:0;top:410px;width:263px;text-align:center;font-size:10.5px">Lic. H5820194400</p>
      <p class="abs" style="left:0;top:560px;width:263px;text-align:center;font-size:10.5px">PO Box 218 Cedar Falls, NY 11900</p>
    </div>
    <div class="coupon" style="top:430px"><span class="coupon__amount">$100 OFF</span><span class="coupon__note">on signed<br>maintenance contract</span></div>
    <div class="coupon" style="top:498px"><span class="coupon__amount">$50 OFF</span><span class="coupon__note">on first<br>service call</span></div>

    <div class="photo" role="img" aria-label="Photo of technicians servicing a rooftop air conditioning unit" style="left:524px;top:100px;width:276px;height:370px;background:linear-gradient(170deg,#c9d3dc 0%,#8e9aa5 45%,#5a4f48 100%)"></div>
    <svg class="abs" style="left:524px;top:0" width="276" height="150" viewBox="0 0 276 150">
      <path d="M0 0H276V128C200 140 90 135 0 100Z" fill="var(--blue)"/>
      <path d="M0 100C90 135 200 140 276 128V136C200 148 90 143 0 108Z" fill="var(--orange)"/>
    </svg>
    <div class="brand" style="left:530px;top:30px;width:264px">
      <div class="brand__row"><span class="brand__dot"></span><span class="brand__name">Bluestem Valley</span></div>
      <div class="brand__tag">AIR CONDITIONING · REFRIGERATION · HEATING</div>
    </div>
    <svg class="abs" style="left:524px;top:440px" width="276" height="60" viewBox="0 0 276 60">
      <path d="M0 20C90 28 200 12 276 0V60H0Z" fill="#fff"/>
      <path d="M0 16C90 24 200 8 276 -4V2C200 14 90 30 0 22Z" fill="var(--orange)"/>
    </svg>
    <div class="feature" style="left:550px;top:447px"><div class="feature__disc"></div><div class="feature__label">AIR CONDITIONING</div></div>
    <div class="feature" style="left:627px;top:447px"><div class="feature__disc"></div><div class="feature__label">REFRIGERATION</div></div>
    <div class="feature" style="left:701px;top:447px"><div class="feature__disc"></div><div class="feature__label">HEATING</div></div>
    <div class="market">COMMERCIAL - RESIDENTIAL</div>
    <div class="availability">24-Hour Emergency Service Available</div>

    <footer class="footer">
      <svg class="abs" style="left:0;top:0" width="800" height="33" viewBox="0 0 800 33">
        <rect width="800" height="33" fill="var(--navy)"/>
        <rect width="800" height="33" fill="var(--blue)" opacity=".55"/>
        <path d="M245 33L262 0H270L253 33Z" fill="var(--orange)"/><path d="M259 33L276 0H282L265 33Z" fill="#fff"/>
        <path d="M510 33L527 0H535L518 33Z" fill="var(--orange)"/><path d="M524 33L541 0H547L530 33Z" fill="#fff"/>
      </svg>
      <span class="footer__text" style="left:23px">24-Hour Emergency Service Available</span>
      <span class="footer__text footer__phone" style="left:330px">
        <svg width="16" height="16" viewBox="0 0 16 16"><circle cx="8" cy="8" r="7" fill="none" stroke="#fff" stroke-width="1.4"/><path d="M5.4 4.4l1.3 1.4-.7 1c.5 1 1.3 1.8 2.3 2.3l1-.7 1.4 1.3-.9 1.2C7.6 10.6 5.2 8.3 4.7 5.3Z" fill="#fff"/></svg>
        555 014 0199</span>
      <span class="footer__text footer__web" style="left:580px">www.bluestemvalleyhvac.com</span>
    </footer>
  </section>

  <!-- ============ INSIDE SPREAD ============ -->
  <section class="spread spread--inside" aria-label="Brochure inside">

    <div class="blue-panel" style="left:0;width:267px;height:587px">
      <div class="brand" style="left:0;top:42px;width:267px">
        <div class="brand__row"><span class="brand__dot"></span><span class="brand__name">Bluestem Valley</span></div>
        <div class="brand__tag">AIR CONDITIONING · REFRIGERATION · HEATING</div>
      </div>
      <div class="headline abs" style="left:0;top:138px;width:267px">EMERGENCY SERVICE<br>WHEN YOU NEED IT</div>
      <div class="inside-copy">
        <p class="body-copy">From complete installation of new systems, to humidifiers and damper motors, we have the experience to get the job done at an affordable price. Our staff is professional and fully licensed, and customer service is our main priority.</p>
        <p class="body-copy">It is our goal to meet all of your needs while providing the best quality service around.</p>
        <p class="install-title">WE SERVICE &amp; INSTALL</p>
        <ul class="install-list">
          <li>Walk-In Coolers &amp; Freezers</li>
          <li>Reach-In Coolers &amp; Freezers</li>
          <li>Ice Machines</li>
          <li>Commercial refrigeration</li>
          <li>Air conditioning (duct, ductless, and rooftop)</li>
        </ul>
        <p class="body-copy">Specializing in diagnosing refrigeration systems for performance issues or safety hazards, we implement accurate, prompt and lasting repairs and are always on-call for 24/7 Emergency Service.</p>
        <p class="body-copy">Our dedication to your complete satisfaction makes all the difference.</p>
      </div>
    </div>

    <div class="photo" role="img" aria-label="Photo of stainless steel reach-in refrigerators in a commercial kitchen" style="left:267px;top:0;width:534px;height:260px;background:linear-gradient(180deg,#d7dadd 0%,#a8aeb4 55%,#7f868d 100%)"></div>
    <svg class="abs" style="left:267px;top:150px" width="534" height="140" viewBox="0 0 534 140">
      <path d="M0 110C120 150 330 120 534 20V140H0Z" fill="#fff"/>
      <path d="M0 106C120 146 330 116 534 16V24C330 124 120 154 0 114Z" fill="var(--orange)"/>
    </svg>
    <svg class="abs" style="left:535px;top:145px" width="240" height="110" viewBox="0 0 240 110" role="img" aria-label="Product photos of a commercial refrigerated display and ice machines, framed in gear shapes">
      <circle cx="50" cy="55" r="50" fill="var(--orange)"/><circle cx="50" cy="55" r="45" fill="#eceff2"/>
      <circle cx="168" cy="52" r="56" fill="var(--orange)"/><circle cx="168" cy="52" r="51" fill="#eceff2"/>
    </svg>

    <div class="plans">
      <div class="plan plan--gold">
        <div class="plan__head">GOLD</div>
        <div class="plan__price">$546</div>
        <ul class="plan__rows">
          <li>MAINTENANCE</li><li>WATER FILTRATION</li>
          <li class="gap">CLEAN COMPLETELY</li><li>USE APPROVED CHEMICALS</li>
          <li class="gap">CLEANING TOOLS</li><li>ALTERNATIVE TREATMENTS</li><li>RUN A PRODUCTION CHECK</li>
        </ul>
      </div>
      <div class="plan plan--silver">
        <div class="plan__head">SILVER</div>
        <div class="plan__price">$702</div>
        <ul class="plan__rows">
          <li>MAINTENANCE</li><li>WATER FILTRATION</li>
          <li class="gap">CLEAN COMPLETELY</li><li>USE APPROVED CHEMICALS</li>
          <li class="gap">CLEANING TOOLS</li><li>ALTERNATIVE TREATMENTS</li><li>RUN A PRODUCTION CHECK</li>
        </ul>
      </div>
      <div class="plan plan--bronze">
        <div class="plan__head">BRONZE</div>
        <div class="plan__price">$858</div>
        <ul class="plan__rows">
          <li>MAINTENANCE</li><li>WATER FILTRATION</li>
          <li class="gap">CLEAN COMPLETELY</li><li>USE APPROVED CHEMICALS</li>
          <li class="gap">CLEANING TOOLS</li><li>ALTERNATIVE TREATMENTS</li><li>RUN A PRODUCTION CHECK</li>
        </ul>
      </div>
    </div>

    <footer class="footer">
      <svg class="abs" style="left:0;top:0" width="801" height="33" viewBox="0 0 801 33">
        <rect width="801" height="33" fill="var(--navy)"/>
        <rect width="801" height="33" fill="var(--blue)" opacity=".55"/>
        <path d="M245 33L262 0H270L253 33Z" fill="var(--orange)"/><path d="M259 33L276 0H282L265 33Z" fill="#fff"/>
        <path d="M510 33L527 0H535L518 33Z" fill="var(--orange)"/><path d="M524 33L541 0H547L530 33Z" fill="#fff"/>
      </svg>
      <span class="footer__text" style="left:23px">24-Hour Emergency Service Available</span>
      <span class="footer__text footer__phone" style="left:330px">
        <svg width="16" height="16" viewBox="0 0 16 16"><circle cx="8" cy="8" r="7" fill="none" stroke="#fff" stroke-width="1.4"/><path d="M5.4 4.4l1.3 1.4-.7 1c.5 1 1.3 1.8 2.3 2.3l1-.7 1.4 1.3-.9 1.2C7.6 10.6 5.2 8.3 4.7 5.3Z" fill="#fff"/></svg>
        555 014 0199</span>
      <span class="footer__text footer__web" style="left:580px">www.bluestemvalleyhvac.com</span>
    </footer>
  </section>

</div>
</body>
</html>
```